Bright Harbor Solar Company Letter Head

We need a clean, branded letterhead built with our company logo. We uploaded some of our promotional marketing material to show you what style we like.

Industry/Entity Type

It Company

Font styles to use
Serif
Sans Serif

Requirements
Must have
• Company Name: Bright Harbor Solar
• Contractors License Number RBQC: 2748315
• Address: 5216 Marlowe Blvd #340 Sacramento, CA 95834
• Phone Number: 916-738-2097
• Fax Number: 916-738-2097

```html
<!DOCTYPE html>
<html lang="en">
<head>
<meta charset="utf-8">
<title>Bright Harbor Solar Letterhead</title>
<link rel="stylesheet" href="https://fonts.googleapis.com/css2?family=Poppins:wght@700&family=PT+Sans:wght@400;700&display=swap">
<style>
  :root {
    --orange: #f26522;
    --orange-deep: #e0501a;
    --ink: #1a1a1a;
    --text: #333333;
    --paper: #ffffff;
  }
  * { margin: 0; padding: 0; box-sizing: border-box; }
  html, body { width: 853px; height: 1200px; overflow: hidden; background: var(--paper); }
  .letterhead { position: relative; width: 853px; height: 1200px; background: var(--paper); font-family: "PT Sans", sans-serif; color: var(--text); }
  .header-waves, .footer-waves { position: absolute; left: 0; display: block; }
  .header-waves { top: 0; }
  .footer-waves { top: 1040px; }
  .brand { position: absolute; left: 14px; top: 40px; display: flex; align-items: center; gap: 10px; }
  .brand-mark { width: 52px; height: 52px; background: var(--orange); }
  .brand-text { display: flex; flex-direction: column; }
  .brand-name { font-family: "Poppins", sans-serif; font-weight: 700; font-size: 27px; line-height: 1.05; color: var(--ink); }
  .brand-tagline { font-family: "PT Sans", sans-serif; font-weight: 700; font-size: 12px; color: var(--ink); margin-top: 4px; }
  .footer { position: absolute; left: 0; top: 1148px; width: 853px; height: 52px; }
  .partner { position: absolute; left: 18px; top: 6px; display: flex; align-items: center; gap: 6px; }
  .partner-dot { width: 22px; height: 22px; border-radius: 50%; background: var(--orange); }
  .partner-name { font-family: "PT Sans", sans-serif; font-weight: 700; font-size: 17px; color: var(--orange-deep); }
  .contact { position: absolute; left: 226px; top: 4px; font-size: 15px; line-height: 1.45; color: var(--text); }
  .contact-lines { display: flex; gap: 34px; padding-left: 30px; }
  .contact-item { display: flex; align-items: center; gap: 8px; }
  .contact-item svg { display: block; }
  .license { position: absolute; right: 18px; top: 4px; font-size: 15px; color: var(--text); }
</style>
</head>
<body>
<div class="letterhead">
  <svg class="header-waves" width="853" height="140" viewBox="0 0 853 140" aria-hidden="true">
    <path d="M0 0 H853 V58 C700 36 520 50 380 78 C300 94 250 104 200 100 C120 94 60 40 0 22 Z" fill="var(--orange)"/>
    <path d="M0 0 H853 V40 C680 26 520 36 400 58 C320 72 270 84 230 84 C150 84 80 30 0 10 Z" fill="var(--orange-deep)" opacity="0.55"/>
    <path d="M230 118 C330 112 420 84 560 66 C680 52 780 54 853 62 V72 C770 64 690 66 580 80 C440 98 340 122 230 118 Z" fill="var(--ink)"/>
  </svg>

  <div class="brand">
    <div class="brand-mark"></div>
    <div class="brand-text">
      <span class="brand-name">Bright Harbor Solar</span>
      <span class="brand-tagline">A Lumenfield Partner Company</span>
    </div>
  </div>

  <svg class="footer-waves" width="853" height="100" viewBox="0 0 853 100" aria-hidden="true">
    <path d="M0 34 C160 40 360 60 560 74 C690 82 780 80 853 76 V92 C760 98 660 98 540 92 C360 82 170 62 0 52 Z" fill="var(--orange)"/>
    <path d="M0 26 C170 30 370 48 560 64 C690 74 780 74 853 70 V76 C780 82 690 84 560 76 C360 62 160 42 0 36 Z" fill="var(--ink)"/>
  </svg>

  <footer class="footer">
    <div class="partner">
      <span class="partner-dot"></span>
      <span class="partner-name">Lumenfield</span>
    </div>
    <div class="contact">
      <div>5216 Marlowe Blvd #340 Sacramento, CA 95834</div>
      <div class="contact-lines">
        <span class="contact-item">
          <svg width="18" height="14" viewBox="0 0 18 14" aria-hidden="true"><rect x="0" y="2" width="18" height="12" rx="2" fill="var(--orange)"/><rect x="4" y="0" width="10" height="4" fill="var(--orange-deep)"/></svg>
          916-738-2097
        </span>
        <span class="contact-item">
          <svg width="18" height="16" viewBox="0 0 18 16" aria-hidden="true"><path d="M1 6 C1 2 17 2 17 6 L14 8 L12 5 H6 L4 8 Z" fill="var(--orange)"/><rect x="4" y="8" width="10" height="7" rx="1" fill="var(--orange)"/></svg>
          916-738-2097
        </span>
      </div>
    </div>
    <div class="license">License Number: 2748315</div>
  </footer>
</div>
</body>
</html>
```